Website design for an events management company

What we need is the design of a website to be used by an events management company, the company is called "Vanto Events Management" and the website is expected to contain the following sections:
1) Homepage
2) Who are we?
3) Mission / Vision / Core values
4) Why to choose Vanto?
5) Past experience
6) Duties or provided services (Scientific Program Duties, Accreditation, Fund Raising, Accommodations, Social Activities, Transportation, Marketing of the Event, Publications and printed materials, Secretarial Work and Media Coverage)
7) References
8) Contact Us page (will probably contain a contact us form plus email, address and a google map)

Attached for your reference the company's logo

Expected that the winner should deliver the designs of at least two pages (the homepage plus an inner page) plus of course all the used graphics, images ... etc.

Thanks

Target Market(s)

The design need to target scientific events and not public events, for example the company doesn't organize music concerts ... etc., it organizes only scientific events so please target business users (i.e. doctors, engineers, scientisits ... etc) while making the designs, including the correct colors, images and icons

Industry/Entity Type

It Company

Number of Pages Required

2 page

Requirements
Must have
• One homepage
• One inner page
• All the used graphics and images
Nice to have
• More than two pages

```html
<!DOCTYPE html>
<html lang="en">
<head>
<meta charset="utf-8">
<title>Vanto Events Management</title>
<link href="https://fonts.googleapis.com/css2?family=Roboto+Condensed:wght@400;500&family=Mulish:wght@400;600;700&display=swap" rel="stylesheet">
<style>
:root{
  --orange:#f7941d;
  --purple:#8b2a8b;
  --deep-purple:#5b2c83;
  --green:#5f9e2f;
  --lime:#7dc243;
  --blue:#1fa3dc;
  --yellow:#f5d20a;
  --red:#e5202e;
  --grey-bar:#6d6e71;
  --header-bg:#f4f4f4;
  --text:#555;
  --field-border:#cfcfcf;
}
*{box-sizing:border-box;margin:0;padding:0}
html,body{width:681px;height:1200px;overflow:hidden;background:#fff}
body{position:relative;font-family:"Mulish",Arial,sans-serif;color:var(--text)}
.abs{position:absolute}

/* header */
.site-header{left:0;top:0;width:681px;height:83px;background:var(--header-bg)}
.brand{left:44px;top:22px;display:flex;align-items:center;gap:8px}
.brand-dot{width:22px;height:22px;border-radius:50%;background:var(--purple)}
.brand-name{font-family:"Mulish",sans-serif;font-weight:700;font-size:24px;color:var(--grey-bar);line-height:1}
.contact-item{top:24px;display:flex;align-items:center;gap:5px;font-family:"Roboto Condensed",sans-serif;font-size:14.5px}
.contact-icon{width:34px;height:34px;border-radius:50%;border:2.5px solid;display:flex;align-items:center;justify-content:center;background:#fff}
.phone{left:242px;color:var(--blue)}
.phone .contact-icon{border-color:var(--purple)}
.email{left:408px;color:var(--orange)}
.email .contact-icon{border-color:var(--lime)}
.header-divider{left:398px;top:31px;width:1px;height:20px;background:#bbb}

/* nav */
.main-nav{left:0;top:83px;width:681px;height:32px;background:var(--grey-bar)}
.main-nav a{position:absolute;top:0;height:32px;line-height:32px;color:#fff;text-decoration:none;font-family:"Roboto Condensed",sans-serif;font-size:12px;letter-spacing:.2px}
.main-nav a.active{background:var(--orange);left:44px;width:62px;text-align:center}

/* hero */
.hero{left:0;top:115px;width:681px;height:258px;
  background:linear-gradient(180deg,#8fa9c9 0%,#c8b9c6 30%,#f1b98c 58%,#e7a04f 78%,#8a8a2c 100%)}
.hero-quote{left:0;top:88px;width:681px;text-align:center;font-family:"Roboto Condensed",sans-serif;font-size:22.5px;line-height:32px;color:#1b1b1b}

/* services */
.section-title{left:0;top:396px;width:681px;text-align:center;font-size:26px;color:var(--purple);font-weight:400}
.services{left:35px;top:444px;width:612px;display:grid;grid-template-columns:repeat(4,153px);grid-template-rows:148px 154px 150px}
.service{text-align:center}
.service-icon{width:60px;height:60px;margin:0 auto;border:1.6px solid var(--orange);border-radius:50%;display:flex;align-items:center;justify-content:center}
.service-title{height:30px;margin-top:4px;display:flex;align-items:center;justify-content:center;font-size:11.5px;line-height:17px;color:var(--green)}
.service-desc{margin-top:6px;font-size:8.8px;line-height:14px;color:#555}

/* rainbow divider */
.rainbow{left:0;top:910px;width:681px;height:3px;display:flex}
.rainbow span{flex:1}

/* footer */
.footer-heading{top:934px;font-size:13px;font-weight:400}
.useful{left:44px}
.useful h3{color:var(--orange)}
.touch h3{color:var(--red)}
.location h3{color:var(--deep-purple)}
.footer-links{left:44px;top:958px;list-style:none}
.footer-links li{font-size:9.5px;line-height:17.6px;color:#555}
.footer-links li:first-child{color:var(--deep-purple)}
.calendar{left:44px;top:1070px}
.field{left:252px;width:177px;height:20px;border:1px solid var(--field-border);background:#fff;font-size:7.5px;color:#888;padding:5px 5px 0}
.field.select{display:flex;justify-content:space-between}
.field.message{height:47px}
.submit{left:252px;top:1119px;width:70px;height:19px;background:var(--orange);color:#fff;font-size:9.5px;font-weight:700;text-align:center;line-height:19px;letter-spacing:.3px}
.map{left:460px;top:960px;width:177px;height:102px;background:linear-gradient(135deg,#e9e6df,#d9dccf 60%,#c9d7e0)}
.social{top:1080px;width:34px;height:34px;border-radius:50%;border:2.5px solid}
.legal-bar{left:0;top:1164px;width:681px;height:36px;background:var(--grey-bar);color:#ececec;font-size:7.5px;text-align:center;line-height:36px}
.legal-bar strong{font-weight:600;color:#fff}
</style>
</head>
<body>
<svg width="0" height="0" style="position:absolute">
  <defs>
    <symbol id="i-atom" viewBox="0 0 40 40"><g fill="none" stroke="#f7941d" stroke-width="1.6"><ellipse cx="20" cy="20" rx="16" ry="6"/><ellipse cx="20" cy="20" rx="16" ry="6" transform="rotate(60 20 20)"/><ellipse cx="20" cy="20" rx="16" ry="6" transform="rotate(-60 20 20)"/></g><circle cx="20" cy="20" r="3" fill="#f7941d"/></symbol>
    <symbol id="i-hands" viewBox="0 0 40 40"><path d="M3 16l8-4 9 6 9-6 8 4-6 10-11 6-11-6z" fill="#f7941d"/></symbol>
    <symbol id="i-fund" viewBox="0 0 40 40"><circle cx="22" cy="11" r="7" fill="none" stroke="#f7941d" stroke-width="1.6"/><text x="22" y="15" font-size="10" text-anchor="middle" fill="#f7941d" font-family="Arial" font-weight="700">$</text><path d="M6 26h10l6 3h8l4-4v3l-6 6H14l-8-3z" fill="#f7941d"/></symbol>
    <symbol id="i-doc" viewBox="0 0 40 40"><rect x="10" y="5" width="20" height="29" rx="2" fill="none" stroke="#f7941d" stroke-width="1.8"/><path d="M14 12h12M14 17h12M14 22h12" stroke="#f7941d" stroke-width="1.8"/><circle cx="15" cy="28" r="1.5" fill="#f7941d"/><path d="M20 28l2 2 4-4" stroke="#f7941d" stroke-width="1.6" fill="none"/></symbol>
    <symbol id="i-plane" viewBox="0 0 40 40"><path d="M6 22l8-2 6-12h3l-2 11 9-2 3-4h2l-1 6 1 6h-2l-3-4-9-2 2 11h-3l-6-12-8-2z" fill="#f7941d" transform="rotate(-20 20 20)"/></symbol>
    <symbol id="i-board" viewBox="0 0 40 40"><rect x="7" y="7" width="26" height="18" fill="none" stroke="#f7941d" stroke-width="1.8"/><rect x="11" y="11" width="7" height="6" fill="#f7941d"/><path d="M21 12h8M21 16h8M11 21h18M20 25v4M14 35l6-6 6 6" stroke="#f7941d" stroke-width="1.6" fill="none"/></symbol>
    <symbol id="i-book" viewBox="0 0 40 40"><path d="M11 6l16 3v27l-16-3z" fill="#f7941d"/><path d="M27 9l3-2v26l-3 3" fill="none" stroke="#f7941d" stroke-width="1.6"/></symbol>
    <symbol id="i-check" viewBox="0 0 40 40"><rect x="9" y="7" width="18" height="24" rx="1" fill="none" stroke="#f7941d" stroke-width="1.6"/><path d="M13 13h10M13 17h10M13 21h6" stroke="#f7941d" stroke-width="1.4"/><circle cx="27" cy="26" r="7" fill="#f7941d"/><path d="M23.5 26l2.5 2.5 4.5-5" stroke="#fff" stroke-width="1.8" fill="none"/></symbol>
    <symbol id="i-news" viewBox="0 0 40 40"><rect x="9" y="8" width="24" height="25" fill="none" stroke="#f7941d" stroke-width="1.8"/><rect x="13" y="12" width="16" height="5" fill="#f7941d"/><path d="M13 21h16M13 25h16M13 29h16M9 12H6v19a2 2 0 004 0" stroke="#f7941d" stroke-width="1.5" fill="none"/></symbol>
  </defs>
</svg>

<header class="site-header abs">
  <div class="brand abs"><span class="brand-dot"></span><span class="brand-name">Vanto</span></div>
  <div class="contact-item phone abs">
    <span class="contact-icon"><svg width="16" height="16" viewBox="0 0 24 24"><path d="M6.6 10.8a15 15 0 006.6 6.6l2.2-2.2a1 1 0 011-.25 11.4 11.4 0 003.6.6 1 1 0 011 1V20a1 1 0 01-1 1A17 17 0 013 4a1 1 0 011-1h3.5a1 1 0 011 1c0 1.25.2 2.45.6 3.6a1 1 0 01-.25 1z" fill="#8b2a8b"/></svg></span>
    <span>010 - 2345 - 6789</span>
  </div>
  <div class="header-divider abs"></div>
  <div class="contact-item email abs">
    <span class="contact-icon"><svg width="14" height="14" viewBox="0 0 24 24" fill="none" stroke="#7dc243" stroke-width="2"><rect x="3" y="5" width="18" height="14" rx="1"/><path d="M3 6l9 7 9-7"/></svg></span>
    <span>info@vantoevents.com</span>
  </div>
</header>

<nav class="main-nav abs">
  <a class="active" href="#">HOME</a>
  <a href="#" style="left:125px">ABOUT</a>
  <a href="#" style="left:196px">SERVICES</a>
  <a href="#" style="left:280px">EXPERIENCE</a>
  <a href="#" style="left:378px">REFERNCE</a>
  <a href="#" style="left:466px">CONTACT</a>
</nav>

<section class="hero abs" role="img" aria-label="Photograph of a rainbow over a colourful sunset sky and countryside fields">
  <p class="hero-quote abs">NOTHING IS IMPOSSIBLE... EVEN THE WORD<br>ITSELF SAYS I'M POSSIBLE</p>
</section>

<h2 class="section-title abs">Vanto Services</h2>
<div class="services abs">
  <div class="service"><div class="service-icon"><svg width="40" height="40"><use href="#i-atom"/></svg></div><div class="service-title">Scientific Program Duties</div><p class="service-desc">Performing all tasks according<br>to a clear time frame.</p></div>
  <div class="service"><div class="service-icon"><svg width="40" height="40"><use href="#i-hands"/></svg></div><div class="service-title">Accreditation</div><p class="service-desc">Preparation of the application<br>forms needed...</p></div>
  <div class="service"><div class="service-icon"><svg width="40" height="40"><use href="#i-fund"/></svg></div><div class="service-title">Fund Raising</div><p class="service-desc">Preparing the preliminary<br>event budget.</p></div>
  <div class="service"><div class="service-icon"><svg width="40" height="40"><use href="#i-doc"/></svg></div><div class="service-title">Accommodations &amp;<br>Social Activities</div><p class="service-desc">Reserving different venues<br>with variable prices</p></div>

  <div class="service"><div class="service-icon"><svg width="40" height="40"><use href="#i-plane"/></svg></div><div class="service-title">Transportation</div><p class="service-desc">Shuttle buses from different<br>hotels or meeting points.</p></div>
  <div class="service"><div class="service-icon"><svg width="40" height="40"><use href="#i-board"/></svg></div><div class="service-title">Marketing of the Event</div><p class="service-desc">Preparation and execution of a<br>professional marketing</p></div>
  <div class="service"><div class="service-icon"><svg width="40" height="40"><use href="#i-book"/></svg></div><div class="service-title">Publications &amp; printed<br>materials</div><p class="service-desc" style="margin-top:-2px">Announcements, flyers,<br>brochures,... etc</p></div>
  <div class="service"><div class="service-icon"><svg width="40" height="40"><use href="#i-check"/></svg></div><div class="service-title">Secretarial Work</div><p class="service-desc">Sending all publications to the<br>available database.</p></div>

  <div class="service"><div class="service-icon"><svg width="40" height="40"><use href="#i-news"/></svg></div><div class="service-title">Media Coverage</div><p class="service-desc">Press conference: to be<br>arranged one week...</p></div>
  <div class="service"><div class="service-icon"><svg width="40" height="40"><use href="#i-atom"/></svg></div><div class="service-title">Scientific Program Duties</div><p class="service-desc">Performing all tasks according<br>to a clear time frame.</p></div>
  <div class="service"><div class="service-icon"><svg width="40" height="40"><use href="#i-hands"/></svg></div><div class="service-title">Accreditation</div><p class="service-desc">Preparation of the application<br>forms needed...</p></div>
  <div class="service"><div class="service-icon"><svg width="40" height="40"><use href="#i-fund"/></svg></div><div class="service-title">Fund Raising</div><p class="service-desc">Preparing the preliminary<br>event budget.</p></div>
</div>

<div class="rainbow abs">
  <span style="background:var(--purple)"></span><span style="background:var(--deep-purple)"></span><span style="background:var(--blue)"></span><span style="background:var(--yellow)"></span><span style="background:var(--lime)"></span><span style="background:var(--orange)"></span><span style="background:var(--red)"></span><span style="background:var(--purple)"></span>
</div>

<footer>
  <div class="useful"><h3 class="footer-heading abs" style="left:44px;color:var(--orange)">Useful Links</h3></div>
  <ul class="footer-links abs">
    <li>Home</li><li>About</li><li>Services</li><li>Experience</li><li>Refernce</li><li>Contact</li>
  </ul>
  <svg class="calendar abs" width="52" height="60" viewBox="0 0 52 60">
    <rect x="1" y="8" width="50" height="50" rx="4" fill="var(--blue)"/>
    <rect x="1" y="8" width="50" height="10" rx="3" fill="#1782b3"/>
    <rect x="12" y="2" width="4" height="12" rx="2" fill="var(--blue)" stroke="#fff"/>
    <rect x="36" y="2" width="4" height="12" rx="2" fill="var(--blue)" stroke="#fff"/>
    <g fill="#fff">
      <rect x="6" y="22" width="8" height="7"/><rect x="17" y="22" width="8" height="7"/><rect x="28" y="22" width="8" height="7"/><rect x="39" y="22" width="8" height="7"/>
      <rect x="6" y="33" width="8" height="7"/><rect x="17" y="33" width="8" height="7"/><rect x="28" y="33" width="8" height="7"/><rect x="39" y="33" width="8" height="7"/>
      <rect x="6" y="44" width="8" height="7"/><rect x="17" y="44" width="8" height="7"/><rect x="28" y="44" width="8" height="7"/><rect x="39" y="44" width="8" height="7"/>
    </g>
  </svg>

  <h3 class="footer-heading abs" style="left:254px;color:var(--red)">Get In Touch</h3>
  <div class="field abs" style="top:960px">Enter Name:</div>
  <div class="field abs" style="top:986px">Enter Email:</div>
  <div class="field abs" style="top:1013px">Enter Title:</div>
  <div class="field select abs" style="top:1039px"><span>Enter Services</span><svg width="9" height="6" viewBox="0 0 9 6"><path d="M0 0h9L4.5 5z" fill="var(--blue)"/></svg></div>
  <div class="field message abs" style="top:1066px">Enter Message</div>
  <div class="submit abs">SUBMIT</div>

  <h3 class="footer-heading abs" style="left:460px;color:var(--deep-purple)">Our Location</h3>
  <div class="map abs" role="img" aria-label="Street map showing the company location"></div>
  <span class="social abs" style="left:459px;border-color:var(--deep-purple)" aria-label="Social link"></span>
  <span class="social abs" style="left:506px;border-color:var(--lime)" aria-label="Social link"></span>
  <span class="social abs" style="left:554px;border-color:var(--lime)" aria-label="Social link"></span>
  <span class="social abs" style="left:601px;border-color:var(--lime)" aria-label="Social link"></span>

  <div class="legal-bar abs">© <strong>Vanto Events Management</strong> - 2015. All Rights Reserved.</div>
</footer>
</body>
</html>
```